New Chiropractic Office needs a fresh flyer design!

We need a flyer design for our chiropractic office for our hometown based chiropractic office called "Corvale Chiropractic" Dr. Martin Corvale provides chiropractic services including adjustments, xrays and wellness exercises with a fresh approach to chiropractic which focuses on getting your body aligned correctly to be a better you. We dont like to focus on coming in just for pain although that is what most people associate our operation with so we understand that comes with the territory. However we would like our flyers to express health and wellness rather than medical or pain. We would like our flyer to emphasize our "New Patient Special" which includes consultation, exam, xrays and first treatment for only $50. We also accept most insurance plans. Call for an appointment 618-390-2757.

Industry/Entity Type

Office

```html
<!DOCTYPE html>
<html lang="en">
<head>
<meta charset="utf-8">
<title>Corvale Chiropractic – New Patient Special Flyer</title>
<link rel="stylesheet" href="https://fonts.googleapis.com/css2?family=Arimo:wght@400;700&display=swap">
<style>
  :root {
    --backdrop: #e9e6df;
    --paper: #ffffff;
    --olive: #7e8a5f;
    --olive-dark: #5f6a45;
    --orange: #f0a01c;
    --badge: #f3c94e;
    --price-red: #d3242a;
    --ink: #1c1c1c;
    --muted: #6f6f6f;
    --icon-green: #8a9a63;
  }
  * { margin: 0; padding: 0; box-sizing: border-box; }
  html, body {
    width: 1200px; height: 900px; overflow: hidden;
    background: var(--backdrop);
    font-family: "Arimo", Arial, sans-serif;
  }
  .flyer {
    position: absolute; left: 300px; top: 62px;
    width: 600px; height: 776px;
    background: var(--olive);
    overflow: hidden;
    box-shadow: 0 10px 30px rgba(0,0,0,.18);
  }
  .flyer-shapes { position: absolute; inset: 0; width: 600px; height: 776px; }

  .brand {
    position: absolute; left: 36px; top: 30px;
    display: flex; align-items: center; gap: 12px;
  }
  .brand-mark { width: 34px; height: 34px; border-radius: 50%; background: var(--icon-green); }
  .brand-name {
    font-weight: 700; font-size: 17px; letter-spacing: .5px;
    text-transform: uppercase; color: var(--olive-dark);
  }
  .brand-tagline {
    position: absolute; left: 82px; top: 70px;
    font-size: 9px; letter-spacing: 1px; text-transform: uppercase; color: var(--muted);
  }

  .contact { position: absolute; left: 330px; top: 26px; list-style: none; }
  .contact li {
    display: flex; align-items: center; gap: 8px;
    font-size: 11px; color: var(--ink); margin-bottom: 12px;
  }
  .contact-icon {
    width: 20px; height: 20px; border-radius: 50%;
    background: var(--icon-green);
    display: flex; align-items: center; justify-content: center;
  }

  .insurance-note {
    position: absolute; left: 232px; top: 448px;
    font-size: 21px; color: #fff; white-space: nowrap;
    transform: rotate(-25deg); transform-origin: left bottom;
    text-shadow: 0 1px 2px rgba(0,0,0,.25);
  }

  .price-badge {
    position: absolute; left: 60px; top: 550px; width: 180px; height: 180px;
    display: flex; flex-direction: column; align-items: center; justify-content: center;
    transform: rotate(-6deg);
  }
  .price-lead { font-size: 22px; color: var(--price-red); }
  .price-amount { font-size: 68px; font-weight: 700; color: var(--price-red); line-height: .95; }
  .price-amount sup { font-size: 36px; vertical-align: 22px; margin-right: 2px; }

  .offer {
    position: absolute; left: 250px; top: 670px;
    transform: rotate(-8deg); transform-origin: left top;
    color: var(--ink);
  }
  .offer-title { font-size: 18px; line-height: 1.15; white-space: nowrap; }
  .offer-title strong { font-weight: 700; }
  .offer-items { font-size: 15px; line-height: 1.15; margin-top: 8px; white-space: nowrap; }
</style>
</head>
<body>
  <article class="flyer">
    <svg class="flyer-shapes" viewBox="0 0 600 776" aria-hidden="true">
      <defs>
        <linearGradient id="meadow" x1="0" y1="0" x2="1" y2="1">
          <stop offset="0" stop-color="#5c7a34"/>
          <stop offset=".5" stop-color="#9fb862"/>
          <stop offset="1" stop-color="#4f6a2c"/>
        </linearGradient>
      </defs>
      <rect class="header-bg" x="0" y="0" width="600" height="150" fill="var(--paper)"/>
      <path class="swoosh-orange" d="M0 572 Q430 500 600 340 L600 372 Q440 528 0 598 Z" fill="var(--orange)"/>
      <path class="white-band" d="M175 660 L600 600 L600 690 L175 752 Z" fill="var(--paper)"/>
      <circle class="badge-body" cx="150" cy="640" r="72" fill="var(--badge)"/>
      <circle class="badge-edge" cx="150" cy="640" r="78" fill="none" stroke="var(--badge)" stroke-width="14" stroke-dasharray="11 6"/>
      <path class="badge-peel" d="M200 690 L222 700 L206 714 Z" fill="#f7f2e0"/>
    </svg>

    <svg class="flyer-shapes" viewBox="0 0 600 776" role="img"
         aria-label="Photo of a woman stretching her arms wide and breathing in fresh air in a green park">
      <path d="M0 120 Q250 95 600 88 L600 340 Q430 500 0 572 Z" fill="url(#meadow)"/>
    </svg>

    <div class="brand">
      <span class="brand-mark"></span>
      <span class="brand-name">Corvale Chiropractic</span>
    </div>
    <p class="brand-tagline">Health &amp; Wellness</p>

    <ul class="contact">
      <li>
        <span class="contact-icon">
          <svg width="12" height="12" viewBox="0 0 24 24"><path d="M6.6 10.8a15 15 0 0 0 6.6 6.6l2.2-2.2a1 1 0 0 1 1-.25 11.4 11.4 0 0 0 3.6.57 1 1 0 0 1 1 1V20a1 1 0 0 1-1 1A17 17 0 0 1 3 4a1 1 0 0 1 1-1h3.5a1 1 0 0 1 1 1c0 1.25.2 2.450.57 3.6a1 1 0 0 1-.25 1z" fill="#fff"/></svg>
        </span>
        Call for an appointment 618-390-2757
      </li>
      <li>
        <span class="contact-icon">
          <svg width="12" height="12" viewBox="0 0 24 24"><path d="M12 2a7 7 0 0 0-7 7c0 5.2 7 13 7 13s7-7.8 7-13a7 7 0 0 0-7-7zm0 9.5A2.5 2.5 0 1 1 12 6.5a2.5 2.5 0 0 1 0 5z" fill="#fff"/></svg>
        </span>
        1450 Alder Lane, Brenton MI 48190
      </li>
    </ul>

    <p class="insurance-note">We also accept most insurance plans</p>

    <div class="price-badge">
      <span class="price-lead">for only</span>
      <span class="price-amount"><sup>$</sup>50</span>
    </div>

    <div class="offer">
      <p class="offer-title"><strong>New Patient Special</strong> which includes:</p>
      <p class="offer-items">Consultation • Exam • X-Rays • First Treatment</p>
    </div>
  </article>
</body>
</html>
```